Business Card Design Project

New business cards that encompass our new logo.
Looking for -
Name, Title, Cell Phone, Email, Address (2 lines), Main Phone, Fax, and website.
Reason: I don't like the graphics used to show phone, fax, cell, email, web, and address.....
I like the double sided cards with logo's on the back. I do not like the logos for phone, fax, cell, address, email, or web.

```html
<!DOCTYPE html>
<html lang="en">
<head>
<meta charset="utf-8">
<title>Northfield Kitchen Supply — Business Card</title>
<link rel="stylesheet" href="https://fonts.googleapis.com/css2?family=Montserrat:ital,wght@0,400;0,600;1,400&display=swap">
<style>
  :root {
    --paper: #f2f0eb;
    --navy: #1c4584;
    --sky: #a6daf4;
    --sky-light: #ffffff;
    --white: #ffffff;
    --card-shadow: rgba(40, 40, 40, 0.18);
  }
  * { box-sizing: border-box; margin: 0; padding: 0; }
  html, body {
    width: 1200px;
    height: 1032px;
    overflow: hidden;
    background: var(--paper);
    font-family: "Montserrat", Arial, sans-serif;
  }
  .canvas {
    position: relative;
    width: 1200px;
    height: 1032px;
  }
  .card {
    position: absolute;
    top: 373px;
    width: 500px;
    height: 286px;
    box-shadow: 0 3px 10px var(--card-shadow);
  }
  .card-front {
    left: 80px;
    background: radial-gradient(ellipse at center, var(--sky-light) 0%, var(--sky-light) 30%, var(--sky) 100%);
    display: flex;
    align-items: center;
    justify-content: center;
  }
  .company-name {
    color: var(--navy);
    font-size: 26px;
    font-weight: 600;
    letter-spacing: 0.2px;
  }
  .card-back {
    left: 620px;
    background: var(--navy);
    color: var(--white);
  }
  .person {
    position: absolute;
    left: 30px;
    bottom: 44px;
  }
  .person-name {
    font-size: 17px;
    font-weight: 600;
  }
  .person-title {
    font-size: 13px;
    font-style: italic;
    margin-top: 2px;
  }
  .contact {
    position: absolute;
    left: 318px;
    top: 152px;
    font-size: 10px;
    line-height: 1.6;
    letter-spacing: 0.3px;
  }
  .address { margin-bottom: 8px; }
  .contact-list { list-style: none; }
  .contact-label {
    display: inline-block;
    width: 13px;
    font-weight: 600;
  }
  .website { margin-top: 8px; }
</style>
</head>
<body>
  <main class="canvas">
    <section class="card card-front" aria-label="Card front">
      <p class="company-name">Northfield Kitchen Supply</p>
    </section>

    <section class="card card-back" aria-label="Card back">
      <div class="person">
        <p class="person-name">Daniel Reyes</p>
        <p class="person-title">Operational Manager</p>
      </div>
      <div class="contact">
        <p class="address">418 Birch Lane<br>Anchorage, AK 99508</p>
        <ul class="contact-list">
          <li><span class="contact-label">M</span>9421 0357</li>
          <li><span class="contact-label">P</span>907 555 0142</li>
          <li><span class="contact-label">F</span>907 555 0178</li>
          <li><span class="contact-label">E</span>daniel@nfksupply.com</li>
        </ul>
        <p class="website">www.nfksupply.com</p>
      </div>
    </section>
  </main>
</body>
</html>
```